Velmora Business Card

We need a design for business cards for our new company. We are a resident safety and security company company that focuses on senior living communities. we provide Nurse call, Access control, CCTV, Wired and wireless network infrastructure, Wander Management, and much more!

Our logo is the circuit board shield. Representing our high tech security solutions. I would like the business card to bring the same theme with perhaps some circuit board traces around the card similar to our logo

```html
<!DOCTYPE html>
<html lang="en">
<head>
<meta charset="utf-8">
<title>Velmora Business Card</title>
<link rel="stylesheet" href="https://fonts.googleapis.com/css2?family=Cinzel:wght@500&family=Roboto:wght@400&family=Tinos&display=swap">
<style>
  :root {
    --backdrop: #2a2a2a;
    --blue-deep: #0a4fd0;
    --blue-mid: #1a6ff0;
    --blue-bright: #2a8cff;
    --blue-ink: #1a52c8;
    --mark-tint: #1f86e8;
    --white: #ffffff;
    --ink: #1c1c1c;
  }
  * { margin: 0; padding: 0; box-sizing: border-box; }
  html, body { width: 1200px; height: 977px; overflow: hidden; }
  body { background: var(--backdrop); position: relative; }

  .card {
    position: absolute;
    width: 560px;
    height: 320px;
    border-radius: 22px;
    overflow: hidden;
    box-shadow: 0 12px 30px rgba(0,0,0,.45);
  }

  /* Front */
  .card-front {
    left: 90px; top: 110px;
    background: radial-gradient(ellipse at 55% 35%, var(--blue-bright) 0%, var(--blue-mid) 45%, var(--blue-deep) 100%);
  }
  .front-mark {
    position: absolute;
    left: 50%; top: 62px;
    width: 110px; height: 110px;
    margin-left: -55px;
    border-radius: 50%;
    background: rgba(255,255,255,.22);
  }
  .front-wordmark {
    position: absolute;
    left: 0; right: 0; top: 196px;
    text-align: center;
    font-family: "Cinzel", serif;
    font-weight: 500;
    font-size: 50px;
    letter-spacing: 2px;
    color: var(--white);
  }

  /* Back */
  .card-back {
    left: 550px; top: 530px;
    background: var(--white);
  }
  .back-mark {
    position: absolute;
    right: 34px; top: 38px;
    width: 190px; height: 190px;
    border-radius: 50%;
    background: var(--mark-tint);
  }
  .back-wordmark {
    position: absolute;
    left: 38px; top: 44px;
    font-family: "Cinzel", serif;
    font-weight: 500;
    font-size: 50px;
    letter-spacing: 1px;
    color: var(--blue-ink);
  }
  .accent-bar {
    position: absolute;
    left: 0; top: 176px;
    width: 9px; height: 52px;
    background: var(--blue-ink);
  }
  .person-name {
    position: absolute;
    left: 38px; top: 166px;
    font-family: "Cinzel", serif;
    font-weight: 500;
    font-size: 23px;
    color: var(--blue-ink);
  }
  .person-role {
    position: absolute;
    left: 40px; top: 198px;
    font-family: "Roboto", sans-serif;
    font-size: 16px;
    color: var(--ink);
  }
  .contact-list {
    position: absolute;
    left: 40px; top: 228px;
    list-style: none;
    font-family: "Tinos", serif;
    font-size: 15px;
    line-height: 20px;
    color: var(--ink);
  }
  .contact-list li { display: flex; align-items: center; gap: 8px; }
  .contact-list svg { width: 13px; height: 13px; fill: var(--blue-ink); flex: none; }
</style>
</head>
<body>

  <section class="card card-front" aria-label="Card front">
    <div class="front-mark"></div>
    <div class="front-wordmark">VELMORA</div>
  </section>

  <section class="card card-back" aria-label="Card back">
    <div class="back-mark"></div>
    <div class="back-wordmark">VELMORA</div>
    <div class="accent-bar"></div>
    <div class="person-name">MARA ELLISON</div>
    <div class="person-role">President</div>
    <ul class="contact-list">
      <li>
        <svg viewBox="0 0 16 16" aria-hidden="true"><path d="M2 5c0-2 2-3 6-3s6 1 6 3v1h-3V5H5v1H2z M4 7h8l2 7H2z"/></svg>
        (555) 210-4482
      </li>
      <li>
        <svg viewBox="0 0 16 16" aria-hidden="true"><path d="M4 1l3 3-2 2c1 2 3 4 5 5l2-2 3 3-2 2C7 14 2 9 2 3z"/></svg>
        (555) 318-7706
      </li>
      <li>
        <svg viewBox="0 0 16 16" aria-hidden="true"><path d="M1 3h14v10H1z M1 3l7 6 7-6" stroke="#fff" stroke-width="1"/></svg>
        Mara@Velmora.com
      </li>
      <li>
        <svg viewBox="0 0 16 16" aria-hidden="true"><circle cx="8" cy="8" r="7"/><path d="M1 8h14M8 1c-3 4-3 10 0 14M8 1c3 4 3 10 0 14" stroke="#fff" stroke-width="1" fill="none"/></svg>
        www.Velmora.com
      </li>
    </ul>
  </section>

</body>
</html>
```